Gourmet Restaurant take out menu

We need a take out menu design that is trendy for a casual upscale Italian restaurant with a vast menu. This menu must be able to be 4 color and reproducible in large quantities to be bulked mailed or inserted into a daily paper. It must also maintain a theme that can be crossed over to our in house dining menu and specials menu.
OUR WEBSITE:
www.velmorabistrohouse.example
For the content, go to the Menu section of our website. We are interested in the design scheme and a template to use.
Target Market(s)
families, sinle individuals seeking take out meals and delivery
Industry/Entity Type
Restaurant

```html
<!DOCTYPE html>
<html lang="en">
<head>
<meta charset="utf-8">
<title>Velmora Bistro House – Take Out Menu</title>
<link href="https://fonts.googleapis.com/css2?family=Oswald:wght@400;500;600&family=Open+Sans:wght@400;600;700&display=swap" rel="stylesheet">
<style>
:root{
  --orange:#e2701e;
  --orange-dark:#c95e14;
  --ink:#2f2f2f;
  --muted:#6a6a6a;
  --paper:#fbfaf7;
  --backdrop:#e9e5dc;
}
*{box-sizing:border-box;margin:0;padding:0}
html,body{width:1200px;height:817px;overflow:hidden;background:var(--backdrop)}
body{font-family:"Open Sans",Arial,sans-serif;color:var(--ink)}
.sheet{position:absolute;left:45px;top:18px;width:1110px;height:781px;display:flex;background:var(--paper);box-shadow:0 6px 18px rgba(0,0,0,.18)}
.panel{width:370px;height:100%;position:relative;border-right:1px solid #e4e0d8;overflow:hidden}
.panel:last-child{border-right:none}

/* inside left panel */
.panel--left{padding:0 22px 0 22px}
.band-head{background:var(--orange);color:#fff;font-family:"Oswald",Arial,sans-serif;font-weight:500;font-size:15px;letter-spacing:.5px;padding:9px 22px;margin:26px -22px 8px;display:flex;justify-content:space-between}
.band-head small{font-size:9px;letter-spacing:.3px;align-self:center}
.section-title{font-family:"Oswald",Arial,sans-serif;font-weight:500;font-size:17px;color:var(--orange);margin:12px 0 5px;text-transform:uppercase}
.section-title--dark{color:var(--ink);border-bottom:2px solid var(--orange);padding-bottom:2px;display:flex;justify-content:space-between;align-items:flex-end}
.section-title--dark .note{font-size:8px;color:var(--orange);display:flex;align-items:center;gap:3px}
.item{display:flex;justify-content:space-between;gap:8px;font-size:7.4px;line-height:1.32;margin-bottom:2px}
.item b{font-weight:700}
.item span.desc{color:var(--muted)}
.item .price{font-weight:600;white-space:nowrap}

/* middle panel */
.panel--middle{display:flex;flex-direction:column}
.mid-top{padding:18px 22px 8px;border:1.5px solid var(--orange);margin:16px 16px 10px}
.mid-top .section-title{margin-top:0;color:var(--ink);text-align:center}
.kids-bev{background:var(--orange);color:#fff;display:flex;gap:10px;padding:12px 14px}
.kids-bev .box{flex:1;border:1px solid rgba(255,255,255,.85);padding:6px 8px}
.kids-bev h3{font-family:"Oswald",Arial,sans-serif;font-weight:500;font-size:14px;text-align:center;margin-bottom:4px}
.kids-bev .item{font-size:7.4px;color:#fff}
.catering{padding:16px 24px 0;text-align:center;font-family:"Oswald",Arial,sans-serif;text-transform:uppercase}
.catering p{font-size:19px;line-height:1.12;font-weight:500}
.phone{display:flex;justify-content:center;align-items:center;gap:6px;color:var(--orange);font-size:24px;font-weight:600;line-height:1.15}
.address{font-family:"Open Sans",Arial,sans-serif;text-transform:none;font-size:14px;margin-top:10px}
.web{font-family:"Open Sans",Arial,sans-serif;text-transform:none;font-size:10px;color:var(--muted);margin-top:3px}
.web b{color:var(--ink)}

/* cover panel */
.brand{margin:20px 16px 0;border:2px solid var(--orange);padding:5px;background:#fff}
.brand-inner{border:1px solid var(--orange);padding:22px 10px 14px;text-align:center}
.brand-name{font-family:"Oswald",Arial,sans-serif;font-weight:500;font-size:52px;color:var(--orange);line-height:1}
.brand-sub{font-family:"Oswald",Arial,sans-serif;font-weight:500;font-size:11px;color:var(--orange);letter-spacing:3px;margin-top:6px}
.cover-photo{position:absolute;left:0;right:0;top:150px;bottom:0;background:radial-gradient(ellipse at 45% 50%,#c8432a 0%,#a8321f 30%,#e8d3a4 55%,#ece6dc 75%,#b96a2c 100%)}
.cover-label{position:absolute;right:28px;bottom:20px;font-family:"Oswald",Arial,sans-serif;font-weight:500;font-size:18px;color:#fff}
</style>
</head>
<body>
<div class="sheet">

  <section class="panel panel--left">
    <div class="band-head">CHICKEN &amp; VEAL <small>ALL ENTREES SERVED WITH BREAD</small></div>
    <div class="item"><span><b>Chicken Parmigiana</b> <span class="desc">breaded cutlet, marinara, melted mozzarella</span></span><span class="price">16.99</span></div>
    <div class="item"><span><b>Chicken Marsala</b> <span class="desc">mushrooms in a rich marsala wine sauce</span></span><span class="price">17.99</span></div>
    <div class="item"><span><b>Chicken Francese</b> <span class="desc">egg battered, lemon butter white wine sauce</span></span><span class="price">17.99</span></div>
    <div class="item"><span><b>Chicken Piccata</b> <span class="desc">capers, lemon and butter sauce</span></span><span class="price">17.99</span></div>
    <div class="item"><span><b>Veal Saltimbocca</b> <span class="desc">prosciutto, sage, spinach and fontina</span></span><span class="price">19.99</span></div>
    <div class="item"><span><b>Veal Sorrentino</b> <span class="desc">eggplant, prosciutto, mozzarella, plum tomato</span></span><span class="price">19.99</span></div>
    <div class="item"><span><b>Veal Parmigiana</b> <span class="desc">breaded veal, marinara, mozzarella cheese</span></span><span class="price">18.99</span></div>

    <h2 class="section-title">Fish and Seafood</h2>
    <div class="item"><span><b>Scallops Piccata</b> <span class="desc">sautéed scallops in a lemon caper butter sauce, served over rice</span></span><span class="price">21.99</span></div>
    <div class="item"><span><b>Flounder Francese</b> <span class="desc">egg battered flounder in a lemon butter sauce</span></span><span class="price">17.99</span></div>
    <div class="item"><span><b>Fried Flounder</b> <span class="desc">lightly breaded, served with coleslaw and French fries</span></span><span class="price">16.99</span></div>
    <div class="item"><span><b>Broiled Seafood Platter</b> <span class="desc">shrimp, scallops and flounder, lemon butter</span></span><span class="price">24.99</span></div>
    <div class="item"><span><b>Shrimp Scampi</b> <span class="desc">garlic, white wine and butter, served over linguini</span></span><span class="price">19.99</span></div>
    <div class="item"><span><b>Tilapia Oreganata</b> <span class="desc">seasoned crumbs, lemon, finished with fresh basil</span></span><span class="price">17.99</span></div>
    <div class="item"><span><b>Salmon Teriyaki</b> <span class="desc">glazed salmon with sesame seeds and vegetables</span></span><span class="price">19.99</span></div>
    <div class="item"><span><b>Stuffed Flounder</b> <span class="desc">stuffed with jumbo lump crab, lemon butter sauce</span></span><span class="price">21.99</span></div>
    <div class="item"><span><b>Salmon Chardonnay</b> <span class="desc">oven broiled salmon in a chardonnay sauce, mashed potatoes</span></span><span class="price">20.99</span></div>

    <h2 class="section-title section-title--dark">Pasta Specialties
      <span class="note"><svg width="9" height="9" viewBox="0 0 10 10"><circle cx="5" cy="5" r="5" fill="#e2701e"/><path d="M2.6 5.2l1.6 1.6 3.2-3.4" stroke="#fff" stroke-width="1.3" fill="none"/></svg>SERVED WITH A HOUSE SALAD AND BREAD</span></h2>
    <div class="item"><span><b>Baked Lasagna</b> <span class="desc">pasta sheets layered with ricotta, fresh herbs, parmesan and mozzarella</span></span><span class="price">12.99</span></div>
    <div class="item"><span><b>Baked Ziti</b> <span class="desc">ricotta cheese, fresh herbs, tomato sauce, shredded mozzarella</span></span><span class="price">12.99</span></div>
    <div class="item"><span><b>Cheese Ravioli</b> <span class="desc">ricotta filled pasta, topped with tomato sauce</span></span><span class="price">12.99</span></div>
    <div class="item"><span><b>Crab Ravioli</b> <span class="desc">crabmeat and ricotta cheese ravioli in a vodka cream sauce</span></span><span class="price">14.99</span></div>
    <div class="item"><span><b>Gnocchi Pesto</b> <span class="desc">roasted mushrooms, spinach, sundried tomatoes</span></span><span class="price">12.99</span></div>
    <div class="item"><span><b>Gnocchi Genovese</b> <span class="desc">tossed in a vodka cream sauce with sausage and peas</span></span><span class="price">12.99</span></div>
    <div class="item"><span><b>Sunday Pasta</b> <span class="desc">imported pasta with our homemade meatballs and tomato sauce</span></span><span class="price">19.59</span></div>
    <div class="item"><span><b>Fettuccini Alfredo</b> <span class="desc">fettuccini tossed in a creamy alfredo sauce</span></span><span class="price">12.99</span></div>
    <div class="item"><span><b>Linguini and Clams</b> <span class="desc">baby clams, fresh herbs and olive oil, red or white sauce</span></span><span class="price">13.99</span></div>
    <div class="item"><span><b>Manicotti</b> <span class="desc">ricotta filled manicotti topped with tomato sauce and mozzarella</span></span><span class="price">13.99</span></div>
    <div class="item"><span><b>Penne Italiano</b> <span class="desc">chicken breast, Italian sausage, broccoli rabe, roasted peppers</span></span><span class="price">16.99</span></div>
    <div class="item"><span><b>Portobello Ravioli</b> <span class="desc">portobello mushroom stuffed ravioli in a sundried tomato cream sauce</span></span><span class="price">15.99</span></div>
    <div class="item"><span><b>Tortellini Bolognese</b> <span class="desc">cheese filled tortellini tossed in our meat and mushroom sauce</span></span><span class="price">14.99</span></div>
    <div class="item"><span><b>Garden Pasta</b> <span class="desc">roasted red peppers, olives, red onion, asparagus, cherry tomatoes</span></span><span class="price">13.99</span></div>
  </section>

  <section class="panel panel--middle">
    <div class="mid-top">
      <h2 class="section-title">Lighter Fare</h2>
      <div class="item"><span><b>Grilled Chicken Primavera</b> <span class="desc">seasonal vegetables, garlic and olive oil. Calories 420; Protein 32g</span></span><span class="price">14.99</span></div>
      <div class="item"><span><b>Lemon Herb Salmon</b> <span class="desc">served with wild rice and steamed spinach. Calories 390; Fat 12g</span></span><span class="price">16.99</span></div>
      <div class="item"><span><b>Shrimp Fra Diavolo</b> <span class="desc">spicy plum tomato sauce over whole wheat linguini. Calories 450</span></span><span class="price">15.99</span></div>
      <div class="item"><span><b>Penne Giardino</b> <span class="desc">cherry tomatoes, asparagus, goat cheese, fresh basil. Calories 410</span></span><span class="price">12.99</span></div>
      <div class="item"><span><b>Tuna Tagliata</b> <span class="desc">seared tuna, broccoli, sesame seeds. Calories 360; Protein 38g</span></span><span class="price">17.99</span></div>
      <div class="item"><span><b>Grilled Mahi Salad</b> <span class="desc">mixed greens, citrus dressing. Calories 330; Sodium 410mg</span></span><span class="price">13.99</span></div>
    </div>

    <div class="kids-bev">
      <div class="box">
        <h3>CHILDREN'S MENU</h3>
        <div class="item"><span>Cheeseburger and Fries</span><span>5.99</span></div>
        <div class="item"><span>Chicken Fingers and Fries</span><span>6.99</span></div>
        <div class="item"><span>Grilled Cheese and Fries</span><span>5.99</span></div>
        <div class="item"><span>Grilled Chicken and Pasta</span><span>6.99</span></div>
        <div class="item"><span>Spaghetti and Meatball</span><span>6.99</span></div>
        <div class="item"><span>Mac and Cheese</span><span>5.99</span></div>
        <div class="item"><span>Mini Pizza</span><span>5.99</span></div>
        <div class="item"><span>Ravioli and Meatball</span><span>6.99</span></div>
        <div class="item"><span>Sliders (3) and Fries</span><span>6.99</span></div>
      </div>
      <div class="box">
        <h3>BEVERAGES</h3>
        <div class="item"><span>16 oz Bottled Tea</span><span>1.99</span></div>
        <div class="item"><span>House Brewed Iced Tea</span><span>1.99</span></div>
        <div class="item"><span>20 oz Bottles: Cola, Diet Cola, Orange, Ginger Ale, Lemon Lime, Root Beer</span><span>2.59</span></div>
        <div class="item"><span>2 Liter Bottles: Cola, Diet Cola, Orange, Ginger Ale, Lemon Lime</span><span>3.59</span></div>
        <div class="item"><span>16 oz Bottled Water</span><span>1.59</span></div>
      </div>
    </div>

    <div class="catering">
      <p>Have a meeting, big party or need<br>a food catering, just call us at</p>
      <div class="phone"><svg width="16" height="18" viewBox="0 0 16 18"><path d="M4 1l3 4-2 2c1 2 2.5 3.8 4.5 5l2-2 3.5 3-2 3C7 16 1 9 1 3z" fill="#e2701e"/></svg>555 014 2200</div>
      <div class="phone"><svg width="18" height="18" viewBox="0 0 18 18"><rect x="4" y="1" width="10" height="5" fill="#e2701e"/><rect x="1" y="6" width="16" height="7" rx="1" fill="#e2701e"/><rect x="4" y="11" width="10" height="6" fill="#fff" stroke="#e2701e" stroke-width="1.5"/></svg>555 014 7381</div>
      <p>And we will happy to<br>serve everything for you.</p>
      <div class="address">118 W. Larkfield Lane Brookhaven, NJ</div>
      <div class="web">or log on to our website <b>www.velmorabistrohouse.example</b></div>
    </div>
  </section>

  <section class="panel panel--cover">
    <div class="cover-photo" role="img" aria-label="Photograph of spaghetti with meatballs in tomato sauce and a basil leaf in a white bowl"></div>
    <div class="brand">
      <div class="brand-inner">
        <div class="brand-name">Velmora</div>
        <div class="brand-sub">BISTRO HOUSE</div>
      </div>
    </div>
    <div class="cover-label">THE MENU</div>
  </section>

</div>
</body>
</html>
```